BWC's Back Sportsman's Lunch

I need a A4 advertisment for our Sportsman's lunch to feature the following information & images.
Darrow Kestrels Old Boys Club Presents the Wybalong Pools BWC's Back
Sportsman's Long Lunch
Date: Friday 10th March 2023 12.30pm Club Tarrabee
3 course meal plus 4 hour Gold Drinks Package
Featuring: Emcee Kevin Stallard Panel Guests: Trent Holway, Lyle Pember & Jace Hurley Comedian: Todd Fairwick
Tickets $250pp or tables of 12
Ex BWC Player table of 12 $3,300
VIP Plus Ex BWC Player table of 12 $3,900

```html
<!DOCTYPE html>
<html lang="en">
<head>
<meta charset="utf-8">
<title>Sportsman's Long Lunch</title>
<link rel="stylesheet" href="https://fonts.googleapis.com/css2?family=Poppins:ital,wght@0,500;0,600;0,700;0,800;1,800&family=Mr+Dafoe&display=swap">
<style>
  :root {
    --page: #eceeee;
    --paper: #ffffff;
    --ink: #16191b;
    --charcoal: #1d2124;
    --teal: #23e6d9;
    --teal-deep: #17504c;
    --teal-mid: #1f6a65;
    --gold: #f4c542;
    --white: #ffffff;
    --slate: #4d6870;
  }
  * { margin: 0; padding: 0; box-sizing: border-box; }
  html, body { width: 948px; height: 1200px; overflow: hidden; background: var(--page); }
  body { font-family: "Poppins", sans-serif; }
  .poster {
    position: absolute; left: 49px; top: 0; width: 849px; height: 1200px;
    background: var(--paper); overflow: hidden;
  }
  .poster * { position: absolute; }
  .stage {
    left: 0; top: 0; width: 849px; height: 1200px;
    clip-path: polygon(0 172px, 849px 78px, 849px 1200px, 0 1200px);
    background:
      linear-gradient(180deg, rgba(23,80,76,0) 640px, var(--teal-deep) 720px, var(--teal-mid) 1200px),
      radial-gradient(circle at 600px 430px, #3a4045 0, var(--charcoal) 380px);
  }
  .club-name {
    left: 50px; top: 22px; width: 86px;
    font-weight: 800; font-size: 15px; line-height: 1.1; color: var(--ink);
    text-transform: uppercase;
  }
  .presents-tag {
    left: 141px; top: 24px; width: 135px; height: 26px; background: var(--ink);
    color: var(--white); font-weight: 800; font-style: italic; font-size: 19px;
    line-height: 26px; padding-left: 10px;
  }
  .sponsor-name {
    left: 141px; top: 52px; font-weight: 600; font-size: 30px; color: var(--slate);
    white-space: nowrap;
  }
  .title-top {
    left: 46px; top: 150px; font-weight: 800; font-size: 92px; line-height: 1;
    color: var(--white); letter-spacing: 1px; white-space: nowrap;
  }
  .title-main {
    left: 72px; top: 246px; font-weight: 800; font-size: 94px; line-height: 1;
    color: var(--teal); white-space: nowrap;
  }
  .title-bracket { left: 0; top: 0; width: 849px; height: 400px; }
  .emcee-photo {
    left: 474px; top: 357px; width: 375px; height: 381px;
    background: radial-gradient(ellipse at 50% 40%, #4a4d55 0, #23262b 70%, rgba(29,33,36,0) 100%);
  }
  .meal { left: 43px; color: var(--teal); font-weight: 800; line-height: 1; white-space: nowrap; }
  .meal-course { top: 378px; font-size: 42px; }
  .meal-hours { top: 422px; font-size: 72px; }
  .meal-drinks { top: 494px; font-size: 27px; color: var(--gold); }
  .date-day { left: 43px; top: 540px; font-size: 48px; font-weight: 800; color: var(--white); line-height: 1; }
  .date-month { left: 43px; top: 588px; font-size: 24px; font-weight: 700; color: var(--teal); line-height: 1; }
  .date-year { left: 43px; top: 612px; font-size: 66px; font-weight: 800; color: var(--white); line-height: 1; }
  .date-divider { left: 224px; top: 546px; width: 3px; height: 126px; background: var(--white); }
  .venue-time { left: 242px; top: 542px; font-size: 34px; font-weight: 800; color: var(--teal); line-height: 1; }
  .venue-club { left: 242px; top: 578px; font-size: 60px; font-weight: 800; color: var(--white); line-height: 1; }
  .venue-name { left: 242px; top: 640px; font-size: 29px; font-weight: 800; color: var(--white); line-height: 1; }
  .featuring { left: 660px; top: 598px; font-family: "Mr Dafoe", cursive; font-size: 40px; color: var(--white); line-height: 1; }
  .emcee-name {
    left: 560px; top: 642px; width: 270px; text-align: center;
    font-size: 31px; font-weight: 800; color: var(--teal); line-height: 1.05;
  }
  .panel-rule { left: 313px; top: 747px; width: 112px; height: 3px; background: var(--teal-mid); }
  .panel-tag {
    left: 55px; top: 726px; width: 258px; height: 44px; background: var(--teal-mid);
    color: var(--white); font-weight: 700; font-size: 23px; line-height: 44px; text-align: center;
  }
  .guest {
    width: 181px; height: 190px; border: 3px solid var(--teal);
    background: linear-gradient(160deg, #2d3338, #14181b);
  }
  .guest-name {
    right: 10px; bottom: 10px; text-align: right; color: var(--white);
    font-weight: 800; font-size: 16px; line-height: 1.1; text-transform: uppercase;
  }
  .guest-role {
    right: 10px; top: 8px; font-family: "Mr Dafoe", cursive; font-size: 18px; color: var(--white);
  }
  .guest-1 { left: 62px; top: 790px; }
  .guest-2 { left: 252px; top: 769px; }
  .guest-3 { left: 62px; top: 990px; height: 173px; }
  .guest-4 { left: 252px; top: 965px; }
  .tickets-label { left: 472px; top: 705px; font-size: 84px; font-weight: 600; color: var(--white); line-height: 1; }
  .tickets-price {
    left: 474px; top: 790px; width: 318px; height: 80px; background: var(--ink);
    color: var(--white); font-size: 64px; font-weight: 700; line-height: 80px; text-align: center;
  }
  .tickets-tables {
    left: 474px; top: 880px; width: 318px; font-size: 35px; font-weight: 700; color: var(--white);
    line-height: 1; text-align: center; padding-bottom: 10px; border-bottom: 3px solid var(--ink);
  }
  .package-label {
    left: 476px; top: 958px; font-size: 16px; font-weight: 700; color: var(--white); line-height: 1.15;
  }
  .package-price {
    left: 627px; top: 938px; width: 173px; height: 60px; background: var(--white);
    color: var(--ink); font-size: 46px; font-weight: 800; line-height: 60px; text-align: center;
  }
  .vip-label {
    left: 474px; top: 1008px; width: 326px; font-size: 21px; font-weight: 700; color: var(--white);
    line-height: 1; text-align: center; padding-bottom: 6px; border-bottom: 3px solid var(--ink);
  }
  .vip-band {
    left: 474px; top: 1042px; width: 326px; height: 44px; background: #0f2c2a;
  }
  .vip-text { left: 14px; top: 0; font-size: 24px; font-weight: 700; color: var(--white); line-height: 44px; }
  .vip-price {
    right: 0; top: 0; width: 132px; height: 44px; background: var(--ink);
    color: var(--white); font-size: 32px; font-weight: 800; line-height: 44px; text-align: center;
  }
</style>
</head>
<body>
<main class="poster">
  <div class="club-name">Darrow Kestrels Old Boys Club</div>
  <div class="presents-tag">PRESENTS</div>
  <div class="sponsor-name">Wybalong Pools</div>

  <div class="stage"></div>

  <h1 class="title-top">SPORTSMAN'S</h1>
  <h2 class="title-main">LONG LUNCH</h2>
  <svg class="title-bracket" viewBox="0 0 849 400" aria-hidden="true">
    <path d="M52 262 V352 H770" fill="none" stroke="#23e6d9" stroke-width="9"/>
    <rect x="760" y="340" width="40" height="24" rx="6" fill="#23e6d9"/>
    <path d="M800 338 H836 M800 346 H836 M800 354 H836 M800 362 H836" stroke="#23e6d9" stroke-width="4"/>
  </svg>

  <div class="emcee-photo" role="img" aria-label="Photo of emcee Kevin Stallard in a dark suit"></div>

  <p class="meal meal-course">3 COURSE MEAL</p>
  <p class="meal meal-hours">+ 4 HOUR</p>
  <p class="meal meal-drinks">GOLD DRINKS PACKAGE</p>

  <p class="date-day">FRIDAY</p>
  <p class="date-month">10TH MARCH</p>
  <p class="date-year">2023</p>
  <div class="date-divider"></div>
  <p class="venue-time">12.30PM</p>
  <p class="venue-club">CLUB</p>
  <p class="venue-name">TARRABEE</p>

  <p class="featuring">Featuring</p>
  <p class="emcee-name">EMCEE KEVIN<br>STALLARD</p>

  <div class="panel-rule"></div>
  <div class="panel-tag">PANEL GUESTS</div>

  <div class="guest guest-1" role="img" aria-label="Photo of panel guest Trent Holway">
    <span class="guest-name">Trent<br>Holway</span>
  </div>
  <div class="guest guest-2" role="img" aria-label="Photo of panel guest Lyle Pember">
    <span class="guest-name">Lyle<br>Pember</span>
  </div>
  <div class="guest guest-3" role="img" aria-label="Photo of panel guest Jace Hurley">
    <span class="guest-name">Jace<br>Hurley</span>
  </div>
  <div class="guest guest-4" role="img" aria-label="Photo of comedian Todd Fairwick with guitar">
    <span class="guest-role">comedian</span>
    <span class="guest-name">Todd<br>Fairwick</span>
  </div>

  <p class="tickets-label">TICKETS</p>
  <p class="tickets-price">$250PP</p>
  <p class="tickets-tables">OR TABLES OF 12</p>

  <p class="package-label">EX BWC PLAYER<br>TABLE OF 12</p>
  <p class="package-price">$3,300</p>

  <p class="vip-label">VIP PLUS EX BWC PLAYER</p>
  <div class="vip-band">
    <span class="vip-text">TABLE OF 12</span>
    <span class="vip-price">$3,900</span>
  </div>
</main>
</body>
</html>
```